Website Design - Photo Shop Design - Functional Cash Register Layout for POS System

Design a webpage for Point of Sale site. A cash register page.

Page must have a good look. I have attached a file of a possible layout example - but need a much nicer design. I have also attached the site logo. which i will upload without background tomorrow hopefully.

Looking for a nice Fresh look , not dark and dingy.

Target Market(s)

Business

Industry/Entity Type

Business Software

Number of Pages Required

1 page

Colors
f59195
f04a50
ec1f27
fbd4d5
ffffff
f8f3f8
fdf0f6
feeeee
ecf5f6

Requirements
Must have
• Cash register layout for POS software site. Nice layout ,
Nice to have
• Try putting he register part on the left side as well as the right - invert the designs have them different to the layout example shown too.
Should not have
• Not to dark

```html
<!DOCTYPE html>
<html lang="en">
<head>
<meta charset="utf-8">
<title>TillNest – Cash Register</title>
<link href="https://fonts.googleapis.com/css2?family=Montserrat:wght@300;400&family=Roboto:wght@400;500&display=swap" rel="stylesheet">
<style>
:root{
  --pink-soft:#fbd4d5;
  --pink-mid:#f59195;
  --red:#f04a50;
  --red-deep:#ec1f27;
  --page:#fdeef3;
  --tile:#f4eded;
  --row:#f3eeee;
  --line:#f0dcdc;
  --text:#333;
  --muted:#777;
  --white:#fff;
}
*{box-sizing:border-box;margin:0;padding:0}
html,body{width:1200px;height:751px;overflow:hidden}
body{position:relative;background:var(--page);font-family:Roboto,Arial,sans-serif;color:var(--text);font-size:12px}
.abs{position:absolute}
.topbar{left:0;top:0;width:1200px;height:64px;background:var(--pink-soft)}
.brand{left:0;top:0;width:180px;height:64px;background:var(--white);display:flex;align-items:center;padding-left:16px;gap:8px}
.brand-dot{width:18px;height:18px;border-radius:50%;background:var(--red)}
.brand-name{font-size:20px;font-weight:500;color:var(--red)}
.register-btn{left:204px;top:17px;width:185px;height:30px;background:var(--pink-mid);color:#fff;font-size:12px;display:flex;align-items:center;padding-left:11px;gap:14px}
.badge{display:inline-flex;align-items:center;justify-content:center;width:16px;height:16px;border-radius:50%;background:#fff;color:var(--red);font-size:10px}
.badge.red{background:var(--red);color:#fff;position:absolute;right:12px}
.search{left:409px;top:17px;width:207px;height:30px;background:#fff;display:flex;align-items:center;gap:8px;padding-left:10px;color:#999;font-size:12px}
.icon{top:22px}
.sidebar{left:0;top:64px;width:180px;height:687px;background:#fff}
.avatar{left:13px;top:87px;width:51px;height:51px;border-radius:50%;background:linear-gradient(#e9d6c8,#c9b1a1)}
.greet{left:75px;top:98px;font-size:13px;line-height:16px}
.greet .role{color:var(--red);font-size:12px}
.menu{left:0;top:160px;width:180px;list-style:none}
.menu li{position:relative;height:40px;display:flex;align-items:center;padding-left:38px;border-bottom:1px solid var(--line);font-size:12.5px}
.menu li.active{height:33px;background:var(--pink-mid);color:#fff}
.menu .mi{position:absolute;left:10px;top:50%;margin-top:-9px;width:18px;height:18px;background:var(--red);border:2px solid #fbd4d5}
.menu li.active .mi{background:var(--red)}
.store-badge{left:16px;top:693px;width:120px;height:36px;border-radius:5px;background:var(--pink-soft)}
.panel{background:#fff}
.products{left:203px;top:91px;width:664px;height:584px}
.panel-head{height:36px;border-bottom:2px solid var(--page);display:flex;align-items:center;padding-left:16px;gap:8px;font-size:14px}
.tile{width:112px;height:100px;background:var(--tile);font-family:Montserrat,sans-serif}
.tile .code{display:block;text-align:center;font-weight:300;font-size:40px;color:#b3a7a7;line-height:80px}
.tile .label{position:absolute;left:0;bottom:0;width:100%;height:20px;background:var(--pink-mid);color:#fff;font-family:Roboto,sans-serif;font-size:11.5px;text-align:center;line-height:20px;white-space:nowrap;overflow:hidden;text-overflow:ellipsis;padding:0 4px}
.pager{width:77px;height:32px;background:#eeeaea;color:#777;text-align:center;line-height:32px;font-size:12px}
.catbar{left:203px;top:695px;width:664px;height:32px;background:var(--red);display:flex;color:#fff;font-size:12.5px}
.catbar span{display:flex;align-items:center;padding:0 13px;border-right:1px solid #f37176}
.catbar .arrow{width:32px;justify-content:center;padding:0}
.catbar .fill{flex:1;border-right:1px solid #f37176}
.customer{left:893px;top:91px;width:282px;height:584px}
.txn{height:29px;background:var(--row);padding-left:14px;display:flex;align-items:center;font-size:12px}
.txn b{font-weight:400;color:var(--red-deep)}
.notes{left:14px;top:383px;color:var(--red-deep);text-decoration:underline;font-size:12px}
.totals{left:0;top:405px;width:282px}
.totals div{height:23.5px;background:var(--row);border-bottom:1px solid #fff;display:flex;justify-content:space-between;align-items:center;padding:0 18px 0 14px;font-size:12px}
.totals span:last-child{color:var(--red-deep)}
.btn{top:540px;height:30px;color:#fff;text-align:center;line-height:30px;font-size:12.5px;letter-spacing:.3px}
.save{left:16px;width:118px;background:var(--pink-mid);opacity:.8;border:1px solid var(--red)}
.pay{left:150px;width:116px;background:var(--red)}
.chat{left:1133px;top:695px;width:42px;height:32px;background:var(--red);display:flex;align-items:center;justify-content:center}
</style>
</head>
<body>
<header class="abs topbar"></header>
<div class="abs brand"><span class="brand-dot"></span><span class="brand-name">TillNest</span></div>
<div class="abs register-btn">My Cash / Cash Register <span class="badge">2</span></div>
<div class="abs search">
  <svg width="12" height="12" viewBox="0 0 12 12"><circle cx="5" cy="5" r="3.6" fill="none" stroke="#f04a50" stroke-width="1.6"/><path d="M8 8l3 3" stroke="#f04a50" stroke-width="1.6"/></svg>Search
</div>
<svg class="abs icon" style="left:639px" width="18" height="18" viewBox="0 0 18 18"><circle cx="9" cy="9" r="5.5" fill="none" stroke="#ec1f27" stroke-width="3" stroke-dasharray="2.2 1.4"/><circle cx="9" cy="9" r="3" fill="none" stroke="#ec1f27" stroke-width="2"/></svg>
<svg class="abs icon" style="left:674px" width="18" height="18" viewBox="0 0 18 18"><circle cx="9" cy="9" r="7" fill="none" stroke="#ec1f27" stroke-width="1.8"/><path d="M9 4.5V9h3.5" fill="none" stroke="#ec1f27" stroke-width="1.8"/></svg>
<svg class="abs" style="left:1153px;top:24px" width="22" height="16" viewBox="0 0 22 16"><path d="M0 1.5h22M0 8h22M0 14.5h22" stroke="#ec1f27" stroke-width="2.4"/></svg>

<aside class="abs sidebar"></aside>
<div class="abs avatar" role="img" aria-label="User profile photo"></div>
<div class="abs greet">Hi, Alex Mercer<br><span class="role">Admin</span></div>
<ul class="abs menu">
  <li class="active"><span class="mi"></span>Enter Sale</li>
  <li><span class="mi"></span>Parked/Layby Orders</li>
  <li><span class="mi"></span>Completed Sales<span class="badge red">3</span></li>
  <li><span class="mi"></span>Appointments<span class="badge red">5</span></li>
  <li><span class="mi"></span>Back Office<span class="badge red">2</span></li>
  <li><span class="mi"></span>Refresh Data</li>
</ul>
<div class="abs store-badge" role="img" aria-label="App store badge"></div>

<section class="abs panel products">
  <div class="panel-head"><span class="brand-dot" style="width:14px;height:14px"></span>Products Stats</div>
</section>
<div class="abs tile" style="left:219px;top:144px"><span class="code">DP</span><span class="label">Demo Product</span></div>
<div class="abs tile" style="left:349px;top:144px"><span class="code">EL</span><span class="label">Entry Level Co...</span></div>
<div class="abs tile" style="left:479px;top:144px"><span class="code">GC</span><span class="label">Gift Cards</span></div>
<div class="abs tile" style="left:608px;top:144px"><span class="code">P5</span><span class="label">Product 5</span></div>
<div class="abs tile" style="left:737px;top:144px"><span class="code">T2</span><span class="label">Test 2</span></div>
<div class="abs tile" style="left:219px;top:261px"><span class="code">T3</span><span class="label">Test 3</span></div>
<div class="abs tile" style="left:349px;top:261px"><span class="code">FA</span><span class="label">fasdfadfasdf</span></div>
<div class="abs tile" style="left:479px;top:261px"><span class="code">P3</span><span class="label">Product 3</span></div>
<div class="abs tile" style="left:608px;top:261px"><span class="code">T3</span><span class="label">Test 3</span></div>
<div class="abs tile" style="left:737px;top:261px"><span class="code">DP</span><span class="label">Demo Product</span></div>
<div class="abs tile" style="left:349px;top:379px"><span class="code">EL</span><span class="label">Entry Level Co...</span></div>
<div class="abs tile" style="left:479px;top:379px"><span class="code">GC</span><span class="label">Gift Cards</span></div>
<div class="abs tile" style="left:608px;top:379px"><span class="code">DP</span><span class="label">Demo Product</span></div>
<div class="abs pager" style="left:219px;top:631px">Previous</div>
<div class="abs pager" style="left:772px;top:631px">Next</div>

<nav class="abs catbar">
  <span class="arrow">&#8249;</span><span>LIST ALL</span><span>DEALS</span><span>UNCATEGORIZED</span><span class="fill"></span><span class="arrow" style="border:0">&#8250;</span>
</nav>

<section class="abs panel customer">
  <div class="panel-head" style="border:0;justify-content:space-between;padding-right:16px">
    <span style="display:flex;align-items:center;gap:8px"><svg width="12" height="14" viewBox="0 0 12 14"><circle cx="6" cy="4" r="3.3" fill="#ec1f27"/><path d="M0 14c0-4 2.5-6 6-6s6 2 6 6z" fill="#ec1f27"/></svg>Select Customer</span>
    <svg width="12" height="8" viewBox="0 0 12 8"><path d="M1 1l5 5 5-5" fill="none" stroke="#ec1f27" stroke-width="1.8"/></svg>
  </div>
  <div class="txn">Transaction:&nbsp;<b>#98565</b></div>
  <span class="abs notes">Add Notes</span>
  <div class="abs totals">
    <div><span>Subtotal</span><span>$0.00</span></div>
    <div><span>Tax</span><span>$0.00</span></div>
    <div><span>Discount</span><span>$0.00</span></div>
    <div><span>Total</span><span>$0.00</span></div>
    <div><span>Paid</span><span>$0.00</span></div>
  </div>
  <div class="abs btn save">SAVE &amp; PERK</div>
  <div class="abs btn pay">PAY NOW</div>
</section>
<div class="abs chat"><svg width="18" height="18" viewBox="0 0 18 18"><circle cx="9" cy="8.5" r="7" fill="none" stroke="#fff" stroke-width="1.5"/><path d="M5.5 8.5h7M5.5 11h4" stroke="#fff" stroke-width="1.3"/></svg></div>
</body>
</html>
```